Private Visitenkarte für Naturwissenschaftler
Vielen Dank für die überaus gute und überzeugende Arbeit. Ohne Einschränkung weiterzuempfehlen!
Zielgruppe
Die Zielgruppe sind primär potentielle Arbeitgeber. Diese sind vor allem in der Forschung und Entwicklung im naturwissenschaftlich-technischem Bereich angesiedelt.
Aufgabenstellung
Vorraussetzungen:
1. Die Karte ist zweiseitig bedruckt
2. Auf der Vorderseite steht der Spruch:
"Wenn es schon einem gelungen ist,
so ist es keine Schwierigkeit.
Wenn es noch keinem gelungen ist,
so wird es dafür langsam Zeit!"
3. Auf der Rückseite stehen die Kontaktdaten
4. Auf beiden Seiten ist ein Hintergrund zu sehen.
Die Datei nsg.pdf beinhaltet die sogenannten Navier-Stokesschen Gleichungen. Diese beschreiben Flüssigkeitsströmungen. Der Hintergrund sollte so aufgebaut sein, dass er zum einen diese Gleichungen enthält (exakt wie dargestellt) und zum anderen etwas, dass durch die Gleichungen beschrieben wird, z.B. ein Wasserfall oder der Fluss durch ein Rohr oder auch gerne etwas Abstraktes.
Die Gestaltung also hauptsächlich den Hintergund, sowie Form, Farbe und Ausrichtung des Textes.
Da sich Rufnummern oder E-Mails immer mal ändern, benötige ich am Ende außerdem ein Dateiformat, das das Editieren der Texte erlaubt (am besten als photoshop document).
Anm.: In der Formel ist ein kleiner Fehler, in der zweiten Zeile muss das "u" ein "v" sein

```html
<!DOCTYPE html>
<html lang="de">
<head>
<meta charset="utf-8">
<title>Visitenkarte Konrad Trinkel</title>
<link href="https://fonts.googleapis.com/css2?family=Roboto+Condensed:wght@500&family=Tinos:ital@0;1&display=swap" rel="stylesheet">
<style>
  :root {
    --page: #ffffff;
    --sky-deep: #34496b;
    --sky-mid: #8aa2c4;
    --sky-light: #e6edf6;
    --water-pale: #f2f5fa;
    --teal: #5ea592;
    --teal-fade: rgba(94, 165, 146, 0);
    --ink: #1f3658;
    --white: #ffffff;
    --line: #1d2a3a;
  }
  html, body {
    margin: 0;
    width: 1200px;
    height: 886px;
    overflow: hidden;
    background: var(--page);
  }
  .card {
    position: absolute;
    width: 605px;
    height: 405px;
    overflow: hidden;
    box-shadow: 8px 14px 22px rgba(0, 0, 0, 0.18);
  }
  .card--front { left: 0; top: 2px; }
  .card--back { left: 564px; top: 453px; }

  .backdrop {
    position: absolute;
    inset: 0;
    background:
      linear-gradient(180deg, transparent 0 66%, var(--water-pale) 66% 100%),
      radial-gradient(ellipse 70% 60% at 45% 62%, var(--sky-light) 0%, var(--sky-mid) 55%, var(--sky-deep) 100%);
  }
  .waterline {
    position: absolute;
    left: 0; right: 0;
    height: 3px;
    background: var(--line);
  }
  .band {
    position: absolute;
    left: 0; right: 0; bottom: 0;
  }
  .card--front .waterline { top: 268px; }
  .card--front .band {
    top: 271px;
    background: linear-gradient(90deg, var(--teal-fade) 0%, var(--teal-fade) 45%, rgba(94,165,146,0.45) 65%, var(--teal) 100%);
  }
  .card--back .waterline { top: 263px; }
  .card--back .band {
    top: 266px;
    background: linear-gradient(90deg, var(--teal) 0%, rgba(94,165,146,0.55) 40%, var(--teal-fade) 70%);
  }

  .quote {
    position: absolute;
    right: 291px;
    top: 42px;
    margin: 0;
    font: 500 20px/27.5px "Roboto Condensed", sans-serif;
    color: var(--white);
    text-align: right;
    white-space: nowrap;
    text-shadow: 0 1px 2px rgba(0,0,0,0.25);
  }
  .quote p { margin: 0 0 6px; }

  .equations {
    position: absolute;
    left: 362px;
    top: 322px;
    width: 226px;
    font: 21px/1 "Tinos", serif;
    color: var(--ink);
    text-align: center;
  }
  .eq-row { display: flex; align-items: center; white-space: nowrap; }
  .frac { display: inline-flex; flex-direction: column; align-items: center; margin-right: 2px; }
  .frac .num { border-bottom: 1px solid var(--ink); padding: 0 1px 1px; }
  .frac .den { padding-top: 1px; }
  .eq-second { margin-top: 4px; }
  i { font-style: italic; }

  .identity {
    position: absolute;
    left: 342px;
    top: 63px;
    color: var(--white);
    font-family: "Roboto Condensed", sans-serif;
    font-weight: 500;
    white-space: nowrap;
    text-shadow: 0 1px 2px rgba(0,0,0,0.2);
  }
  .identity .name { font-size: 28px; line-height: 32px; }
  .identity .degree { font-size: 19.5px; line-height: 26px; }

  .contact {
    position: absolute;
    left: 27px;
    top: 301px;
    margin: 0;
    padding: 0;
    list-style: none;
    font: 500 20px/25px "Roboto Condensed", sans-serif;
    color: var(--ink);
  }
  .contact li { display: flex; align-items: center; gap: 8px; }
  .contact svg { width: 21px; height: 21px; flex: none; }
</style>
</head>
<body>

<section class="card card--front">
  <div class="backdrop" role="img" aria-label="Foto: Wasserstrahl, der in eine Wasseroberfläche fließt, mit Spritzern und Luftblasen"></div>
  <div class="waterline"></div>
  <div class="band"></div>

  <blockquote class="quote">
    <p>„Wenn es schon einem gelungen ist,<br>so ist es keine Schwierigkeit.</p>
    <p>Wenn es noch keinem gelungen ist,<br>so wird es dafür langsam Zeit!“</p>
  </blockquote>

  <div class="equations" aria-label="Navier-Stokes-Gleichungen">
    <div class="eq-row">
      <span class="frac"><span class="num">∂v</span><span class="den">∂<i>t</i></span></span>
      <span>&nbsp;+ (v·∇)v = <i>ν</i>△v − ∇<i>p</i> + f</span>
    </div>
    <div class="eq-second">∇· v = 0</div>
  </div>
</section>

<section class="card card--back">
  <div class="backdrop" role="img" aria-label="Foto: Wasserstrahl, der in eine Wasseroberfläche fließt, mit Spritzern und Luftblasen"></div>
  <div class="waterline"></div>
  <div class="band"></div>

  <div class="identity">
    <div class="name">Konrad Trinkel</div>
    <div class="degree">Dipl.-Math. und Dipl.-Phys.</div>
  </div>

  <ul class="contact">
    <li>
      <svg viewBox="0 0 20 20" aria-hidden="true"><circle cx="10" cy="10" r="9" fill="#fff" stroke="#1f3658" stroke-width="1.5"/><path d="M5.5 5l2 0 1 2.5-1.3 1c.6 1.3 1.6 2.3 2.9 2.9l1-1.3 2.5 1v2c-4.5.3-8.4-3.6-8.1-8.1z" fill="#1f3658"/><g fill="#1f3658"><rect x="11" y="5" width="1.3" height="1.3"/><rect x="13" y="5" width="1.3" height="1.3"/><rect x="11" y="7" width="1.3" height="1.3"/><rect x="13" y="7" width="1.3" height="1.3"/></g></svg>
      <span>04561 872390</span>
    </li>
    <li>
      <svg viewBox="0 0 20 20" aria-hidden="true"><circle cx="10" cy="10" r="9" fill="#fff" stroke="#1f3658" stroke-width="1.5"/><rect x="7" y="4.5" width="6" height="11" rx="1" fill="none" stroke="#1f3658" stroke-width="1.5"/><circle cx="10" cy="13.5" r="0.8" fill="#1f3658"/></svg>
      <span>0172 5583016</span>
    </li>
    <li>
      <svg viewBox="0 0 20 20" aria-hidden="true"><circle cx="10" cy="10" r="9" fill="#fff" stroke="#1f3658" stroke-width="1.5"/><text x="10" y="14.5" text-anchor="middle" font-size="14" font-family="Arial, sans-serif" fill="#1f3658">@</text></svg>
      <span>konrad.trinkel@verplux.de</span>
    </li>
  </ul>
</section>

</body>
</html>
```